Accountant services flyer & marketing portfolio

I require a design for a marketing portfolio of blank templates for a flyer, product brochure, report cover for A4 based on our style - current logo, letterhead, website look and feel - that can be updated in publisher or word with relevant marketing and company information editorial material and text. It will be either printed A4 or saved as PDF and distributed

Target Market(s)

small business and investment / superfund clients

Industry/Entity Type

Accountant

Font styles to use
Sans Serif

Requirements
Must have
• Instyle of letterhead and website
Professional body logos
Space to input text
Relevant happy images
Nice to have
• Images of happy lifestyle types retirees, young families and mid-aged
tradesmen and professionals

```html
<!DOCTYPE html>
<html lang="en">
<head>
<meta charset="utf-8">
<title>Horizon Advisory – Think 2021 Flyer</title>
<link href="https://fonts.googleapis.com/css2?family=Roboto:ital,wght@0,100;0,300;0,400;0,500;0,700;0,900;1,300&display=swap" rel="stylesheet">
<style>
  :root{
    --orange:#f05a28;
    --amber:#fbb03b;
    --ink:#1d1d1d;
    --panel:#d1d2d4;
    --white:#ffffff;
  }
  *{margin:0;padding:0;box-sizing:border-box}
  html,body{width:848px;height:1200px;overflow:hidden;background:var(--white)}
  body{font-family:'Roboto',sans-serif;color:var(--ink)}
  .flyer{position:relative;width:848px;height:1200px;overflow:hidden;background:var(--white)}
  .hero-art{position:absolute;left:0;top:0}
  .hero-title{position:absolute;left:388px;top:34px;color:var(--white);line-height:1}
  .hero-title .think{font-weight:900;font-size:60px;letter-spacing:1px;display:block}
  .hero-title .year{font-weight:100;font-size:104px;display:block;margin-top:4px;letter-spacing:-2px}
  .tagline{position:absolute;right:37px;top:296px;text-align:right;color:var(--orange)}
  .tagline .lead{font-weight:700;font-size:28px;line-height:34px;display:block}
  .tagline .focus{font-weight:300;font-style:italic;font-size:35px;line-height:46px;display:block;margin-top:-2px}
  .intro{position:absolute;left:57px;top:472px;width:740px;font-size:16.4px;line-height:20.5px;font-weight:400}
  .services{position:absolute;left:0;top:604px;width:434px;height:355px;background:var(--panel)}
  .services-head{height:52px;background:var(--orange);color:var(--white);padding-left:57px;display:flex;align-items:center;gap:8px}
  .services-head .light{font-weight:300;font-size:32px}
  .services-head .bold{font-weight:700;font-size:23px;margin-top:6px}
  .services-list{list-style:none;padding:20px 0 0 57px}
  .services-list li{font-weight:700;font-size:18.6px;height:46.8px;display:flex;align-items:flex-start;gap:13px}
  .services-list li::before{content:"";width:9px;height:9px;border-radius:50%;background:var(--ink);margin-top:8px;flex:none}
  .key-point{position:absolute;left:475px;width:326px;height:113px;border:1px solid var(--orange)}
  .key-point h3{position:absolute;left:24px;top:-15px;background:var(--white);padding:0 10px 0 5px;font-weight:700;font-size:21.5px;line-height:26px}
  .key-point p{position:absolute;left:29px;top:17px;width:290px;font-size:16.3px;line-height:19.6px}
  .kp1{top:604px}.kp2{top:750px}.kp3{top:896px}
  .brand-mark{position:absolute;left:62px;top:1062px;width:40px;height:40px;border-radius:50%;background:var(--orange)}
  .brand-name{position:absolute;left:158px;top:1070px;font-weight:500;font-size:29px;line-height:34px;color:var(--orange);letter-spacing:-0.5px}
  .brand-strap{position:absolute;left:160px;top:1104px;font-size:19px;line-height:24px;font-weight:400;color:var(--ink)}
  .contact{position:absolute;left:508px;top:1089px;font-size:15.2px;line-height:21.6px;font-style:normal}
  .contact .row{display:flex;align-items:flex-start;gap:10px}
  .contact svg{flex:none;margin-top:4px}
  .contact .phones{display:flex;gap:36px}
  .footer-band{position:absolute;left:0;bottom:0}
  .web{position:absolute;left:95px;top:1166px;color:var(--white);font-weight:700;font-size:18px}
</style>
</head>
<body>
<div class="flyer">
  <svg class="hero-art" width="848" height="460" viewBox="0 0 848 460">
    <defs>
      <linearGradient id="arcGrad" x1="0" y1="1" x2="1" y2="0">
        <stop offset="0" stop-color="#f05a28"/>
        <stop offset="1" stop-color="#fbb03b"/>
      </linearGradient>
      <linearGradient id="photoGrad" x1="0" y1="0" x2="1" y2="1">
        <stop offset="0" stop-color="#3a3a3c"/>
        <stop offset="0.45" stop-color="#8d8f94"/>
        <stop offset="1" stop-color="#c9ccd2"/>
      </linearGradient>
    </defs>
    <circle cx="282" cy="-8" r="435" fill="url(#arcGrad)"/>
    <circle cx="290" cy="-22" r="396" fill="url(#photoGrad)" role="img" aria-label="Photo of a hand holding a pen over financial charts and a calculator on a desk"/>
  </svg>

  <h1 class="hero-title"><span class="think">THINK</span><span class="year">2021</span></h1>

  <p class="tagline">
    <span class="lead">When you</span>
    <span class="lead">think about 2021</span>
    <span class="lead">you must think about</span>
    <span class="focus">Technology, Innovation</span>
  </p>

  <p class="intro">For over 35 years Horizon CEO Martin Hale has prospered on the “Cutting Edge” of Business and Finance. With extensive qualifications, comprehensive and wide ranging hands-on experience, he offers a unique and potent combination of expertise and knowledge that will guarantee superior strategic advice that can really make a difference.</p>

  <section class="services">
    <div class="services-head"><span class="light">Services</span><span class="bold">We offered</span></div>
    <ul class="services-list">
      <li>Tax &amp; Accounting</li>
      <li>Litigation, Audit &amp; Assurance</li>
      <li>Outsource CFO Services</li>
      <li>Business Improvement Stratagies</li>
      <li>Supperanuation &amp; Financial Planning</li>
      <li>Business Reconstruction Services</li>
    </ul>
  </section>

  <div class="key-point kp1"><h3>Key Point : 1</h3><p>Lorem ipsum dolor sit amet, consectetuer adipiscing elit, sed diam nonummy nibh euismod tincidunt ut laoreet dolore</p></div>
  <div class="key-point kp2"><h3>Key Point : 2</h3><p>Lorem ipsum dolor sit amet, consectetuer adipiscing elit, sed diam nonummy nibh euismod tincidunt ut laoreet dolore</p></div>
  <div class="key-point kp3"><h3>Key Point : 3</h3><p>Lorem ipsum dolor sit amet, consectetuer adipiscing elit, sed diam nonummy nibh euismod tincidunt ut laoreet dolore</p></div>

  <span class="brand-mark"></span>
  <p class="brand-name">HORIZON ADVISORY</p>
  <p class="brand-strap">Clear advice. Real results</p>

  <address class="contact">
    <div class="row">
      <svg width="14" height="16" viewBox="0 0 14 16"><path d="M7 0a6 6 0 0 0-6 6c0 4.5 6 10 6 10s6-5.5 6-10a6 6 0 0 0-6-6zm0 8.5A2.5 2.5 0 1 1 7 3.5a2.5 2.5 0 0 1 0 5z" fill="var(--orange)"/></svg>
      <span>Suite 204, Level 2, 58 Harbour View Road<br>Kingsford NSW 2032</span>
    </div>
    <div class="row phones">
      <div class="row">
        <svg width="14" height="14" viewBox="0 0 14 14"><rect width="14" height="14" rx="3" fill="var(--orange)"/><path d="M4 3l2 .5.5 2-1 1a6 6 0 0 0 2.5 2.5l1-1 2 .5.5 2c-4 .5-8-3.5-7.5-7.5z" fill="#fff"/></svg>
        <span>1300 555 014</span>
      </div>
      <div class="row">
        <svg width="10" height="15" viewBox="0 0 10 15"><rect x="0.5" y="0.5" width="9" height="14" rx="1.5" fill="none" stroke="var(--orange)" stroke-width="1.5"/><rect x="2" y="2" width="6" height="9" fill="var(--orange)"/></svg>
        <span>0400 111 222</span>
      </div>
    </div>
    <div class="row">
      <svg width="14" height="11" viewBox="0 0 14 11"><rect width="14" height="11" rx="1" fill="var(--orange)"/><path d="M1 1.5l6 4.5 6-4.5" fill="none" stroke="#fff" stroke-width="1.3"/></svg>
      <span>hello@horizonadvisory.com.au</span>
    </div>
  </address>

  <svg class="footer-band" width="848" height="46" viewBox="0 0 848 46">
    <defs>
      <linearGradient id="bandGrad" x1="0" y1="0" x2="1" y2="0">
        <stop offset="0" stop-color="#f05a28"/>
        <stop offset="1" stop-color="#fbb03b"/>
      </linearGradient>
    </defs>
    <path d="M0 2H405c12 0 18 4 26 12c10 10 18 20 34 20H848V46H0z" fill="url(#bandGrad)"/>
  </svg>
  <p class="web">www.horizonadvisory.com.au</p>
</div>
</body>
</html>
```